Faith Based Film Production Ecommerce Site Needed

We are a faith based film production company that offers coaching services as well as physical and digital products.

We have a Wordpress site on Hostwick. It currently, features a landing page (https://plumfernstudio.com/), however we now need a fully fleshed out interactive website that will feature short videos/trailers as well the ability for customers to make online purchases.

The updated site will feature 5 tabs - Take 1, Take 2, Take 3, BTS and Contact. This toolbar/menu should remain fixed/stable while visitors navigate the different tabs/pages, as shown here - https://dowgenbarsk.com/ (note this site is JUST a reference for its unmoving menu/toolbar in the top right corner of the page).

The text for each tab and actual video content will be provided for potential candidates. Until then, please improvise.

There will be 5 short trailers/reels featured under the "Take 2" tab, that will be shown as thumbnails the same size found here - https://dowgenbarsk.com/see-dowgen-at-work/ (reference for thumbnail size only). The names of these trailers will be called, Lantern Quest, Lantern Blooming, Lantern Dawn, Lantern Hearth, and Lantern Courtship.

Lastly, when arriving onto the page, visitors will be greeted with a inaudible video loop, similar to the one found here - https://www.tq-moviecraft.com/ (Note - this is a reference simply to show inaudible video looping). The ACTUAL video to be used however can be found here - https://clipvault.example/manage/videos/493817265, beginning at the 15 second mark when the 3 people are entering the cinema and ending at the 28 second mark where the screen gradually fades to black. The video will then consistently re-loop.

Once again, more detail will be provided for the most interesting submissions and of course, official winner.

Should you have any questions until then, please do not hesitate to reach out.

```html
<!DOCTYPE html>
<html lang="en">
<head>
<meta charset="utf-8">
<title>Plumfern Studio</title>
<link href="https://fonts.googleapis.com/css2?family=Limelight&family=Lato:wght@400;700&family=Poppins:wght@400;500&display=swap" rel="stylesheet">
<style>
:root{
  --ink:#111111;
  --white:#ffffff;
  --paper:#f5f5f5;
  --body:#2b2b2b;
  --hero-a:#1b1d2a;
  --hero-b:#3a2f2c;
  --footer:#000000;
  --bar:#1c1c1c;
  --display:"Limelight", serif;
  --text:"Lato", sans-serif;
  --ui:"Poppins", sans-serif;
}
*{box-sizing:border-box;margin:0;padding:0}
html,body{width:1200px;height:2646px;overflow:hidden}
body{position:relative;background:var(--white);font-family:var(--text);color:var(--body)}
.hero{position:absolute;left:0;top:0;width:1200px;height:599px;
  background:radial-gradient(ellipse at 40% 40%,#4a3d3a 0%,var(--hero-b) 30%,var(--hero-a) 75%)}
.hero-title{position:absolute;top:296px;width:100%;text-align:center;font-family:var(--display);
  font-size:54px;color:var(--white);letter-spacing:1px}
.nav a{position:absolute;top:37px;font-family:var(--display);font-size:15px;color:var(--white);text-decoration:none;letter-spacing:.5px}
.brand-badge{position:absolute;left:509px;top:-54px;width:182px;height:182px;border-radius:50%;background:var(--white);
  display:flex;align-items:flex-end;justify-content:center;padding-bottom:42px}
.brand-name{font-family:var(--display);font-size:16px;color:var(--ink)}
section{position:absolute;left:0;width:1200px}
.about{top:599px;height:457px;background:var(--paper)}
.works{top:1056px;height:809px;background:var(--white)}
.news{top:1865px;height:379px;background:var(--paper)}
h2{position:absolute;width:100%;text-align:center;font-family:var(--display);font-weight:400;font-size:34px;color:var(--ink)}
.lead{position:absolute;left:190px;width:820px;text-align:center;font-size:15px;line-height:29px}
.btn{position:absolute;background:var(--ink);color:var(--white);font-family:var(--display);font-size:17px;
  display:flex;align-items:center;justify-content:center;border-radius:6px;box-shadow:0 3px 8px rgba(0,0,0,.3)}
.reel{position:absolute;width:303px}
.thumb{width:303px;height:246px;border-radius:6px;position:relative}
.play{position:absolute;left:131px;top:102px;width:42px;height:42px;border-radius:50%;background:rgba(255,255,255,.9)}
.play::after{content:"";position:absolute;left:16px;top:12px;border-left:14px solid var(--ink);border-top:9px solid transparent;border-bottom:9px solid transparent}
.reel-title{margin-top:28px;text-align:center;font-family:var(--display);font-size:19px;color:var(--ink)}
.signup{position:absolute;left:150px;top:234px;width:898px;height:70px;background:var(--white);border-radius:4px;box-shadow:0 2px 10px rgba(0,0,0,.08)}
.signup .field{position:absolute;left:22px;top:24px;font-family:var(--display);font-size:15px;color:#8a8a8a}
footer{position:absolute;left:0;top:2244px;width:1200px;height:338px;background:var(--footer);color:var(--white);font-family:var(--ui)}
.foot-logo{position:absolute;left:111px;top:77px;width:243px;height:161px;background:var(--white);display:flex;align-items:center;justify-content:center}
.foot-logo span{font-family:var(--display);font-size:24px;color:var(--ink)}
.col{position:absolute;top:76px}
.col h3{font-family:var(--display);font-weight:400;font-size:19px;margin-bottom:18px}
.col li{list-style:none;font-size:15.5px;height:34.5px;display:flex;align-items:center}
.col li svg{margin-right:10px}
.contact-row{display:flex;align-items:center;font-size:15.5px;line-height:26px;margin-bottom:20px}
.contact-row .ico{width:32px;height:32px;border-radius:50%;background:var(--white);display:flex;align-items:center;justify-content:center;margin-right:13px;flex:none}
.copy{position:absolute;left:0;top:2582px;width:1200px;height:64px;background:var(--bar);color:var(--white);
  font-size:15px;text-align:center;line-height:64px}
</style>
</head>
<body>

<header class="hero" role="img" aria-label="Video loop of friends in a dark cinema with popcorn and 3D glasses">
  <nav class="nav">
    <a style="left:110px">HOME</a>
    <a style="left:220px">TAKE 1</a>
    <a style="left:354px">TAKE 2</a>
    <a style="left:770px">TAKE 3</a>
    <a style="left:903px">BTS</a>
    <a style="left:1011px">CONTACT</a>
  </nav>
  <div class="brand-badge"><span class="brand-name">PLUMFERN STUDIO</span></div>
  <h1 class="hero-title">WELCOME TO PLUMFERN STUDIO</h1>
</header>

<section class="about">
  <h2 style="top:62px">ABOUT PLUMFERN STUDIO</h2>
  <p class="lead" style="top:115px">Nam libero tempore, cum soluta nobis est eligendi optio cumque nihil impedit quo minus id quod maxime placeat facere possimus, omnis voluptas assumenda est, omnis dolor repellendus. Temporibus autem quibusdam et aut officiis debitis aut rerum necessitatibus saepe eveniet ut et voluptates repudiandae sint et molestiae non recusandae.</p>
  <p class="lead" style="top:232px;left:220px;width:760px">Itaque earum rerum hic tenetur a sapiente delectus, ut aut reiciendis voluptatibus maiores alias consequatur aut perferendis doloribus asperiores repellat.</p>
  <div class="btn" style="left:500px;top:312px;width:200px;height:64px">READ MORE</div>
</section>

<section class="works">
  <h2 style="top:56px">TAKE 2</h2>
  <div class="reel" style="left:111px;top:116px">
    <div class="thumb" role="img" aria-label="Still of a creator filming an unboxing on a phone" style="background:linear-gradient(135deg,#d9d2c8,#9a8f84)"><span class="play"></span></div>
    <div class="reel-title">LANTERN QUEST</div>
  </div>
  <div class="reel" style="left:448px;top:116px">
    <div class="thumb" role="img" aria-label="Still of a white blossom on a branch against the sun" style="background:linear-gradient(135deg,#3c4a66,#1e2233 60%,#6a5b7a)"><span class="play"></span></div>
    <div class="reel-title">LANTERN BLOOMING</div>
  </div>
  <div class="reel" style="left:785px;top:116px">
    <div class="thumb" role="img" aria-label="Still of a person sitting by the water on green grass" style="background:linear-gradient(180deg,#3f7f86,#4f8a8c 65%,#6f8a4a)"><span class="play"></span></div>
    <div class="reel-title">LANTERN DAWN</div>
  </div>
  <div class="reel" style="left:280px;top:447px">
    <div class="thumb" role="img" aria-label="Still of a film projector beaming onto a screen" style="background:linear-gradient(90deg,#1a1a1a,#2e2e2e 45%,#bdbdbd)"><span class="play"></span></div>
    <div class="reel-title">LANTERN HEARTH</div>
  </div>
  <div class="reel" style="left:617px;top:447px">
    <div class="thumb" role="img" aria-label="Still of an expecting couple holding hands outdoors" style="background:linear-gradient(135deg,#6b6a3e,#3e4a2a 55%,#8a8a7a)"><span class="play"></span></div>
    <div class="reel-title">LANTERN COURTSHIP</div>
  </div>
</section>

<section class="news">
  <h2 style="top:59px">JOIN OUR NEWSLETTER</h2>
  <p class="lead" style="top:111px;left:205px;width:790px">Temporibus autem quibusdam et aut officiis debitis aut rerum necessitatibus saepe eveniet ut et voluptates repudiandae sint et molestiae non recusandae.Itaque earum rerum hic tenetur a sapiente delectus, ut aut reiciendis voluptatibus maiores alias consequatur aut perferendis doloribus asperiores repellat.</p>
  <div class="signup">
    <span class="field">Enter The Email</span>
    <div class="btn" style="left:716px;top:4px;width:180px;height:62px;border-radius:4px;box-shadow:none;background:#000">SUBSCRIBE</div>
  </div>
</section>

<footer>
  <div class="foot-logo"><span>PLUMFERN STUDIO</span></div>
  <div class="col" style="left:430px">
    <h3>QUICK LINKS</h3>
    <ul>
      <li><svg width="13" height="12" viewBox="0 0 13 12"><path d="M1 6h10M6 1l5 5-5 5" stroke="#fff" stroke-width="2.4" fill="none"/></svg>Home</li>
      <li><svg width="13" height="12" viewBox="0 0 13 12"><path d="M1 6h10M6 1l5 5-5 5" stroke="#fff" stroke-width="2.4" fill="none"/></svg>Take 1</li>
      <li><svg width="13" height="12" viewBox="0 0 13 12"><path d="M1 6h10M6 1l5 5-5 5" stroke="#fff" stroke-width="2.4" fill="none"/></svg>Take 2</li>
      <li><svg width="13" height="12" viewBox="0 0 13 12"><path d="M1 6h10M6 1l5 5-5 5" stroke="#fff" stroke-width="2.4" fill="none"/></svg>BTS</li>
      <li><svg width="13" height="12" viewBox="0 0 13 12"><path d="M1 6h10M6 1l5 5-5 5" stroke="#fff" stroke-width="2.4" fill="none"/></svg>Contact Us</li>
    </ul>
  </div>
  <div class="col" style="left:663px">
    <h3>HELP LINKS</h3>
    <ul>
      <li><svg width="13" height="12" viewBox="0 0 13 12"><path d="M1 6h10M6 1l5 5-5 5" stroke="#fff" stroke-width="2.4" fill="none"/></svg>FAQ</li>
      <li><svg width="13" height="12" viewBox="0 0 13 12"><path d="M1 6h10M6 1l5 5-5 5" stroke="#fff" stroke-width="2.4" fill="none"/></svg>Terms of use</li>
      <li><svg width="13" height="12" viewBox="0 0 13 12"><path d="M1 6h10M6 1l5 5-5 5" stroke="#fff" stroke-width="2.4" fill="none"/></svg>Privacy Policy</li>
      <li><svg width="13" height="12" viewBox="0 0 13 12"><path d="M1 6h10M6 1l5 5-5 5" stroke="#fff" stroke-width="2.4" fill="none"/></svg>Support Links</li>
      <li style="font-weight:500"><svg width="13" height="12" viewBox="0 0 13 12"><path d="M1 6h10M6 1l5 5-5 5" stroke="#fff" stroke-width="2.4" fill="none"/></svg>Conditions</li>
    </ul>
  </div>
  <div class="col" style="left:888px">
    <h3>CONTACT US</h3>
    <div class="contact-row"><span class="ico"><svg width="14" height="18" viewBox="0 0 14 18"><path d="M7 1a6 6 0 0 0-6 6c0 4.5 6 10 6 10s6-5.5 6-10a6 6 0 0 0-6-6z" fill="#000"/><circle cx="7" cy="7" r="2.2" fill="#fff"/></svg></span><span>Plumfern Studio<br>United States</span></div>
    <div class="contact-row"><span class="ico"><svg width="16" height="16" viewBox="0 0 16 16"><path d="M3 1.5l2.5 0 1.2 3.3-1.6 1.2a9 9 0 0 0 4.9 4.9l1.2-1.6 3.3 1.2 0 2.5a1.5 1.5 0 0 1-1.6 1.5A13 13 0 0 1 1.5 3.1 1.5 1.5 0 0 1 3 1.5z" fill="#000"/></svg></span><span>+1 555 014 2288</span></div>
    <div class="contact-row"><span class="ico"><svg width="16" height="12" viewBox="0 0 16 12"><rect x="0.5" y="0.5" width="15" height="11" rx="1.5" fill="#000"/><path d="M1.5 1.5l6.5 5 6.5-5" stroke="#fff" stroke-width="1.4" fill="none"/></svg></span><span>info@plumfernstudio.com</span></div>
  </div>
</footer>

<div class="copy">Copyrights@2023.Plumfern Studio.All Rights Reserved</div>

</body>
</html>
```